Business Card For Energy Consultancy Company
Vantor Advisory
Business Card For Energy Consultancy Company - Energy
Creative Brief
Simple
Tarek M. Bouzid
Managing Director
P.O. Box 48213, Dubai, United Arab Emirates
+971 4 5827316 ext. 214
tmbouzid@vantoradvisoryltd.example
Please note the following: 1- The final design should allow us FULL flexibility on changing and updating the data to appear on the card. 2- The design of the card must be extremely professional, elegant and simple 3- Our clients will mostly be governments and global utilities (you can check out the following websites of some of our potential clients): - http://www.norvexa.example - http://www.palimorgrid.example/ - http://www.kwo.example/ 4- Please avoid cluttering the card with too many unnecessary stuff, however keep it sophisticated. 5- Please don't use too many colors PLEASE USE THE LOGO THAT WE HAVE UPLOADED
The back will eventually be used to input the contact data in a second language. So please make sure that their is sufficient space to enter the contact details (please indicate with dummy text where the different contact data should go).

```html
<!DOCTYPE html>
<html lang="en">
<head>
<meta charset="utf-8">
<title>Vantor Advisory Stationery Set</title>
<link rel="stylesheet" href="https://fonts.googleapis.com/css2?family=Open+Sans:wght@400;700&display=swap">
<style>
:root{
  --red:#e3262d;
  --black:#1b1b1b;
  --white:#ffffff;
  --paper:#fbfbfb;
  --ink:#555;
  --label:#d8d8d8;
  --bg-top:#8a8a8a;
  --bg-bottom:#3f3f3f;
}
*{margin:0;padding:0;box-sizing:border-box}
html,body{width:1200px;height:446px;overflow:hidden}
body{font-family:"Open Sans",Arial,sans-serif;background:radial-gradient(ellipse at 50% 30%,var(--bg-top),var(--bg-bottom) 85%);position:relative}
.item{position:absolute;box-shadow:0 2px 6px rgba(0,0,0,.45)}
.label{position:absolute;font-size:6px;color:var(--label);text-align:center}
.brand{font-weight:700;color:var(--red);white-space:nowrap;letter-spacing:.2px}
.brand.light{color:var(--white)}
.card{width:108px;height:60px;background:var(--white);overflow:hidden}
.card-front .band{height:18px;background:var(--black);padding:3px 6px;color:var(--white)}
.card-front .name{font-size:5.5px;font-weight:700;line-height:1.2}
.card-front .role{font-size:4px}
.card-front .brand{font-size:8px;position:absolute;left:6px;top:24px}
.contact{position:absolute;left:6px;top:36px;font-size:3.4px;color:var(--ink);line-height:1.5;list-style:none}
.contact li::before{content:"";display:inline-block;width:2.5px;height:2.5px;background:var(--red);margin-right:2px;vertical-align:middle}
.card-back{display:flex;align-items:center;justify-content:center}
.card-back .brand{font-size:10px}
.card-back.red{background:var(--red)}
.letterhead{width:269px;height:388px;background:var(--paper);overflow:hidden}
.letterhead .head-brand{position:absolute;left:14px;top:14px;font-size:15px}
.letterhead .contact{left:auto;right:16px;top:14px;font-size:4px}
.letterhead .foot-band{position:absolute;left:0;right:0;bottom:0;height:9px;background:var(--black)}
.letterhead .foot-rule{position:absolute;left:14px;right:14px;bottom:20px;height:1px;background:var(--red)}
.letterhead .foot-text{position:absolute;left:0;right:0;bottom:11px;font-size:3.6px;color:var(--ink);text-align:center;line-height:1.4}
.letterhead.option-two .foot-rule{bottom:22px;background:#ccc}
.letterhead.option-two .foot-text{bottom:8px}
.foot-brand{display:block;font-size:6px;line-height:1.3}
.envelope{width:317px;height:112px;background:var(--paper);overflow:hidden}
.envelope svg{position:absolute;inset:0}
.envelope .flap-brand{position:absolute;left:0;right:0;text-align:center;font-size:10px}
.envelope .corner-brand{position:absolute;left:10px;top:10px;font-size:10px}
.envelope.red{background:var(--red)}
.envelope.black{background:var(--black)}
.envelope .addr{position:absolute;left:0;right:0;bottom:6px;font-size:3.6px;color:var(--ink);text-align:center}
</style>
</head>
<body>

<div class="item card card-front" style="left:24px;top:108px">
  <div class="band">
    <div class="name">Tarek M. Bouzid</div>
    <div class="role">Managing Director</div>
  </div>
  <div class="brand">Vantor Advisory</div>
  <ul class="contact">
    <li>P.O. Box 48213, Dubai, UAE</li>
    <li>+971 4 5827316 ext. 214</li>
    <li>tmbouzid@vantoradvisoryltd.example</li>
  </ul>
</div>
<div class="label" style="left:24px;top:174px;width:108px">Business Card</div>

<div class="item card card-back red" style="left:24px;top:200px"><span class="brand light">Vantor Advisory</span></div>
<div class="label" style="left:24px;top:266px;width:108px">Back Card Option 1</div>

<div class="item card card-back" style="left:24px;top:296px"><span class="brand">Vantor Advisory</span></div>
<div class="label" style="left:24px;top:362px;width:108px">Back Card Option 2</div>

<div class="item letterhead" style="left:163px;top:18px">
  <div class="brand head-brand">Vantor Advisory</div>
  <ul class="contact">
    <li>P.O. Box 48213, Dubai, United Arab Emirates</li>
    <li>+971 4 5827316 ext. 214</li>
    <li>tmbouzid@vantoradvisoryltd.example</li>
  </ul>
  <div class="foot-rule"></div>
  <div class="foot-text">P.O. Box 48213, Dubai, United Arab Emirates &nbsp;|&nbsp; +971 4 5827316</div>
  <div class="foot-band"></div>
</div>
<div class="label" style="left:163px;top:412px;width:269px">Letterhead option 1</div>

<div class="item letterhead option-two" style="left:439px;top:18px">
  <div class="foot-rule"></div>
  <div class="foot-text"><span class="brand foot-brand">Vantor Advisory</span>P.O. Box 48213, Dubai, United Arab Emirates &nbsp;|&nbsp; +971 4 5827316 &nbsp;|&nbsp; tmbouzid@vantoradvisoryltd.example</div>
</div>
<div class="label" style="left:439px;top:412px;width:269px">Letterhead option 2</div>

<div class="item envelope red" style="left:815px;top:53px;height:120px">
  <svg width="317" height="120" viewBox="0 0 317 120"><polyline points="0,0 158,70 317,0" fill="none" stroke="#fff" stroke-width="1.2"/></svg>
  <div class="brand light flap-brand" style="top:16px">Vantor Advisory</div>
</div>
<div class="item envelope black" style="left:815px;top:125px;height:120px">
  <svg width="317" height="120" viewBox="0 0 317 120"><polyline points="0,0 158,70 317,0" fill="none" stroke="#444" stroke-width="1"/></svg>
  <div class="brand light flap-brand" style="top:26px">Vantor Advisory</div>
</div>
<div class="item envelope" style="left:815px;top:206px;height:94px">
  <svg width="317" height="94" viewBox="0 0 317 94"><polyline points="0,0 158,56 317,0" fill="none" stroke="#ccc" stroke-width="1"/></svg>
  <div class="brand flap-brand" style="top:20px">Vantor Advisory</div>
</div>
<div class="item envelope" style="left:815px;top:288px;height:108px">
  <div class="brand corner-brand">Vantor Advisory</div>
  <div class="addr">P.O. Box 48213, Dubai, United Arab Emirates &nbsp;|&nbsp; +971 4 5827316</div>
</div>
<div class="label" style="left:815px;top:402px;width:317px">Envelope Model Back</div>

</body>
</html>
```